Brand new redesign of Brightwell finance website

I need a new website design that i can advertise a great low interest rate on the front page and capture input application details that will send through to my email address.

some car finance companies will be similar to this would be listed below

quorvaloans.com.au
pelmarfinance.com.au
finance715.com.au
gundrelfinance.com.au
finance93.com.au
Updates

Project Deadline Extended
Reason: I have changed the project to a committed project. all the webpages should have the same format just different content and i want to be able to edit the front page easily to update my interest rates.

Project Deadline Extended
Reason: Provide more time for resubmission and submission work

Target Market(s)

Australian Finance market targeting a younger demographic

Industry/Entity Type

Finance

Coding

Coded - Design and coding required

Number of Pages Required

5+ page

Font styles to use
Serif
Sans Serif

Colors
0255a3
ffffff
cedeed

Requirements
Must have
• application capture form
• apply now buttons
• Headline rate front page

```html
<!DOCTYPE html>
<html lang="en">
<head>
<meta charset="utf-8">
<title>Brightwell Finance – Debt Consolidation</title>
<link rel="stylesheet" href="https://fonts.googleapis.com/css2?family=Roboto:wght@300;400;500;700&family=Roboto+Condensed:wght@400;700&family=Open+Sans:ital,wght@0,400;1,400&display=swap">
<style>
:root{
  --blue:#0255a3;
  --blue-deep:#1f57a6;
  --navy:#234a8c;
  --sky:#cedeed;
  --cyan:#2a8bd1;
  --white:#ffffff;
  --ink:#333a40;
  --muted:#5f6770;
  --line:#dfe3e8;
  --pale:#f3f4f6;
  --footer:#eef0f3;
  --bar:#8c8f94;
  --dark-btn:#2c2f33;
  --star:#1f8b4c;
}
*{box-sizing:border-box;margin:0;padding:0}
html,body{width:1200px;height:2609px;overflow:hidden}
body{position:relative;background:var(--white);font-family:"Roboto",Arial,sans-serif;color:var(--ink)}
.abs{position:absolute}

/* header */
.site-header{position:absolute;left:0;top:0;width:1200px;height:125px;background:var(--white);border-bottom:1px solid var(--line)}
.brand{position:absolute;left:99px;top:30px;display:flex;align-items:center;gap:10px}
.brand-dot{width:40px;height:40px;border-radius:50%;background:var(--blue)}
.brand-name{font-family:"Roboto Condensed",sans-serif;font-weight:700;font-size:20px;line-height:22px;color:var(--blue);width:120px}
.header-phone{position:absolute;left:791px;top:28px;display:flex;align-items:center;gap:10px;font-size:19px;color:var(--ink)}
.btn-apply-top{position:absolute;left:979px;top:24px;width:121px;height:34px;background:var(--cyan);color:var(--white);font-size:13px;display:flex;align-items:center;justify-content:center;letter-spacing:.3px}
.main-nav{position:absolute;top:84px;left:0;width:1200px;font-size:13px;color:var(--ink)}
.main-nav span{position:absolute;white-space:nowrap}
.main-nav .active{color:var(--blue)}

/* hero */
.hero{position:absolute;left:0;top:125px;width:1200px;height:578px;background:linear-gradient(90deg,#f1f8ea 0%,#eef3f6 35%,#c8d4de 60%,#a8b3bd 100%)}
.hero-photo{position:absolute;left:420px;top:0;width:780px;height:578px;background:linear-gradient(120deg,rgba(240,244,247,0) 0%,#c9d4dc 30%,#8a97a3 55%,#b8c2ca 80%,#d9dfe4 100%)}
.hero-kicker{position:absolute;left:99px;top:197px;font-family:"Roboto Condensed",sans-serif;font-weight:700;font-size:30px;color:var(--blue)}
.hero-title{position:absolute;left:99px;top:233px;font-family:"Roboto Condensed",sans-serif;font-weight:700;font-size:40px;color:var(--ink)}
.hero-text{position:absolute;left:99px;top:290px;width:360px;font-size:14px;line-height:22px;color:var(--muted)}
.hero-rate{color:var(--blue);font-weight:700}
.btn-read{position:absolute;left:99px;top:372px;width:124px;height:37px;background:var(--blue);color:var(--white);font-size:13px;display:flex;align-items:center;justify-content:center;border-radius:2px}
.slide-arrow{position:absolute;top:319px;width:34px;height:34px;border-radius:50%;background:rgba(120,125,130,.6);display:flex;align-items:center;justify-content:center}
.apply-panel{position:absolute;left:790px;top:171px;width:311px;height:407px;background:rgba(28,82,160,.92);padding:24px 28px 0}
.apply-panel h2{font-family:"Roboto Condensed",sans-serif;font-weight:400;font-size:25px;color:var(--white);margin-bottom:14px;margin-left:-4px}
.field{height:38px;background:var(--white);margin-bottom:5px;font-size:12px;color:#888;display:flex;align-items:center;padding-left:12px;justify-content:space-between;padding-right:12px}
.btn-signup{margin-top:12px;height:36px;background:var(--dark-btn);color:var(--white);font-size:15px;display:flex;align-items:center;justify-content:center}

/* services */
.services{position:absolute;left:0;top:703px;width:1200px;height:559px;background:var(--pale)}
.section-title{position:absolute;left:0;width:1200px;text-align:center;font-family:"Roboto",sans-serif;font-weight:400;font-size:30px;color:var(--ink)}
.title-rule{position:absolute;left:565px;width:70px;height:2px;background:var(--ink)}
.service-card{position:absolute;top:142px;width:238px;height:338px;background:var(--white);border:1px solid var(--line)}
.service-card h3{height:44px;background:var(--navy);color:var(--white);font-weight:400;font-size:17px;display:flex;align-items:center;justify-content:center}
.service-photo{height:151px}
.service-card p{font-size:12px;line-height:21px;color:var(--ink);text-align:center;padding:14px 18px 0}
.btn-more{position:absolute;left:61px;top:286px;width:116px;height:30px;border:1px solid var(--navy);border-radius:15px;font-size:11px;display:flex;align-items:center;justify-content:center;gap:6px;color:var(--ink)}

/* steps */
.steps{position:absolute;left:0;top:1262px;width:1200px;height:545px;background:linear-gradient(180deg,#1d5dae 0%,#1552a3 100%)}
.steps .section-title{color:var(--white);top:65px}
.step{position:absolute;top:155px;width:300px;text-align:center;color:var(--white)}
.step-icon{width:108px;height:108px;border-radius:50%;background:var(--white);margin:0 auto;display:flex;align-items:center;justify-content:center}
.step h3{font-weight:400;font-size:21px;margin-top:26px}
.step p{font-size:12px;line-height:21px;margin-top:8px;padding:0 25px}
.btn-apply{position:absolute;left:501px;top:432px;width:198px;height:47px;background:var(--sky);color:var(--blue);font-size:17px;display:flex;align-items:center;justify-content:center;border-radius:2px}

/* reviews */
.reviews{position:absolute;left:0;top:1807px;width:1200px;height:388px;background:var(--white)}
.review{position:absolute;top:141px;width:460px;height:156px;border-left:1px solid var(--line);padding-left:28px}
.review blockquote{font-family:"Open Sans",sans-serif;font-style:italic;font-size:14px;line-height:23px;color:var(--muted);max-width:400px}
.reviewer{display:flex;align-items:center;gap:24px;margin-top:26px}
.avatar{width:76px;height:76px;border-radius:50%;background:radial-gradient(circle at 50% 40%,#d9c2ad,#8b7565)}
.reviewer-name{font-family:"Open Sans",sans-serif;font-style:italic;font-size:13px;color:var(--navy)}
.stars{display:flex;gap:2px;margin-top:8px}
.stars span{width:15px;height:15px;background:var(--star);display:flex;align-items:center;justify-content:center}

/* partners */
.partners{position:absolute;left:0;top:2195px;width:1200px;height:104px;background:#f7f8f9;border-top:1px solid var(--line)}
.partner-mark{position:absolute;top:38px;height:30px;background:#c4c8cd;border-radius:3px}

/* footer */
.site-footer{position:absolute;left:0;top:2299px;width:1200px;height:254px;background:var(--footer)}
.footer-brand{position:absolute;left:99px;top:64px;display:flex;flex-direction:column;align-items:center;gap:8px}
.footer-col h4{position:absolute;font-weight:400;font-size:15px;color:var(--ink);top:34px;white-space:nowrap}
.contact-line{position:absolute;left:277px;display:flex;gap:12px;font-size:12px;line-height:19px;color:var(--ink)}
.newsletter-text{position:absolute;left:624px;top:66px;width:290px;font-size:11px;line-height:19px;color:var(--ink)}
.nl-input{position:absolute;left:624px;width:263px;height:40px;background:var(--white);font-size:11px;color:var(--ink);display:flex;align-items:center;padding-left:14px}
.btn-subscribe{position:absolute;left:789px;top:167px;width:98px;height:40px;background:var(--cyan);color:var(--white);font-size:12px;display:flex;align-items:center;justify-content:center}
.info-links{position:absolute;left:970px;top:68px;list-style:none;font-size:11px;line-height:27px;color:var(--ink)}
.copyright{position:absolute;left:0;top:2553px;width:1200px;height:56px;background:var(--bar);color:var(--white);font-size:11px;display:flex;align-items:center;justify-content:center}
</style>
</head>
<body>

<header class="site-header">
  <div class="brand"><span class="brand-dot"></span><span class="brand-name">BRIGHTWELL FINANCE</span></div>
  <div class="header-phone">
    <svg width="18" height="18" viewBox="0 0 24 24"><path fill="#0255a3" d="M6.6 10.8a15.1 15.1 0 0 0 6.6 6.6l2.2-2.2a1 1 0 0 1 1-.25 11.4 11.4 0 0 0 3.6.57 1 1 0 0 1 1 1V20a1 1 0 0 1-1 1A17 17 0 0 1 3 4a1 1 0 0 1 1-1h3.5a1 1 0 0 1 1 1c0 1.25.2 2.45.57 3.57a1 1 0 0 1-.25 1z"/></svg>
    +1300 482 719
  </div>
  <div class="btn-apply-top">APPLY NOW</div>
  <nav class="main-nav">
    <span class="active" style="left:529px">HOME</span>
    <span style="left:600px">ABOUT BRIGHTWELL</span>
    <span style="left:755px">OUR SERVICES</span>
    <span style="left:882px">PRIVACY POLICY</span>
    <span style="left:1023px">CONTACT US</span>
  </nav>
</header>

<section class="hero">
  <div class="hero-photo" role="img" aria-label="Photo of smiling colleagues reviewing finance documents at a laptop"></div>
  <div class="hero-kicker">BRIGHTWELL FINANCE</div>
  <h1 class="hero-title">DEBT CONSOLIDATION</h1>
  <p class="hero-text">Combine your debts into one low repayment with rates from <span class="hero-rate">5.49% p.a.</span> Fast approval, no hidden fees, apply online in minutes.</p>
  <div class="btn-read">READ MORE</div>
  <div class="slide-arrow" style="left:30px"><svg width="12" height="12" viewBox="0 0 12 12"><path d="M8 1 3 6l5 5" stroke="#fff" stroke-width="2" fill="none"/></svg></div>
  <div class="slide-arrow" style="left:1132px"><svg width="12" height="12" viewBox="0 0 12 12"><path d="m4 1 5 5-5 5" stroke="#fff" stroke-width="2" fill="none"/></svg></div>
  <form class="apply-panel">
    <h2>GET STARTED TODAY!</h2>
    <div class="field">First Name :</div>
    <div class="field">Last Name :</div>
    <div class="field">Email :</div>
    <div class="field">Phone :</div>
    <div class="field">State :<svg width="10" height="6" viewBox="0 0 10 6"><path d="M0 0h10L5 6z" fill="#666"/></svg></div>
    <div class="field">Loan amount :</div>
    <div class="btn-signup">SIGN UP NOW</div>
  </form>
</section>

<section class="services">
  <h2 class="section-title" style="top:58px">OUR SERVICES</h2>
  <div class="title-rule" style="top:106px"></div>
  <article class="service-card" style="left:99px">
    <h3>Bas Agent</h3>
    <div class="service-photo" role="img" aria-label="Photo of a couple working on paperwork at a laptop" style="background:linear-gradient(135deg,#e6e1da,#b9a895)"></div>
    <p>Lorem ipsum dolor sit amet, consectt adipiscing elit, sed do eiusmod tepor incididunt ut labore et dolore</p>
    <div class="btn-more">CLICK HERE <svg width="10" height="10" viewBox="0 0 10 10"><circle cx="5" cy="5" r="5" fill="#234a8c"/><path d="m4 3 2 2-2 2" stroke="#fff" fill="none"/></svg></div>
  </article>
  <article class="service-card" style="left:354px">
    <h3>Payroll &amp; Bookkeeping</h3>
    <div class="service-photo" role="img" aria-label="Photo of hands on a laptop showing a payroll screen" style="background:linear-gradient(135deg,#8f7a6a,#4f6f8f)"></div>
    <p>Lorem ipsum dolor sit amet, consectt adipiscing elit, sed do eiusmod tepor incididunt ut labore et dolore</p>
    <div class="btn-more">CLICK HERE <svg width="10" height="10" viewBox="0 0 10 10"><circle cx="5" cy="5" r="5" fill="#234a8c"/><path d="m4 3 2 2-2 2" stroke="#fff" fill="none"/></svg></div>
  </article>
  <article class="service-card" style="left:608px">
    <h3>Credit File Repair</h3>
    <div class="service-photo" role="img" aria-label="Photo of a couple checking their credit file at a computer" style="background:linear-gradient(135deg,#e9e6e2,#b9aea2)"></div>
    <p>Lorem ipsum dolor sit amet, consectt adipiscing elit, sed do eiusmod tepor incididunt ut labore et dolore</p>
    <div class="btn-more">CLICK HERE <svg width="10" height="10" viewBox="0 0 10 10"><circle cx="5" cy="5" r="5" fill="#234a8c"/><path d="m4 3 2 2-2 2" stroke="#fff" fill="none"/></svg></div>
  </article>
  <article class="service-card" style="left:862px">
    <h3>Debt Consolidation</h3>
    <div class="service-photo" role="img" aria-label="Photo of a hand with a pen over financial statements" style="background:linear-gradient(135deg,#efe9e6,#c9b9b4)"></div>
    <p>Lorem ipsum dolor sit amet, consectt adipiscing elit, sed do eiusmod tepor incididunt ut labore et dolore</p>
    <div class="btn-more">CLICK HERE <svg width="10" height="10" viewBox="0 0 10 10"><circle cx="5" cy="5" r="5" fill="#234a8c"/><path d="m4 3 2 2-2 2" stroke="#fff" fill="none"/></svg></div>
  </article>
</section>

<section class="steps">
  <h2 class="section-title">3 STEPS FOR FAST FINANCE</h2>
  <div class="step" style="left:116px">
    <div class="step-icon"><svg width="40" height="40" viewBox="0 0 24 24" fill="none" stroke="#0255a3" stroke-width="1.8"><path d="M11 4H5a1 1 0 0 0-1 1v14a1 1 0 0 0 1 1h14a1 1 0 0 0 1-1v-6"/><path d="M18 3l3 3-9 9H9v-3z"/></svg></div>
    <h3>Apply Online in Minutes</h3>
    <p>Nemo enim ipsam voluptatem quia voluptas sit aspernatur aut odit aut fugit, sed quia consntur magni dolores eos qui ratione</p>
  </div>
  <div class="step" style="left:467px">
    <div class="step-icon"><svg width="40" height="40" viewBox="0 0 24 24" fill="none" stroke="#0255a3" stroke-width="1.8" stroke-linejoin="round"><path d="M21 3 3 10l7 3 3 7z"/><path d="M21 3 10 13"/></svg></div>
    <h3>Fast Approval Process</h3>
    <p>Nemo enim ipsam voluptatem quia voluptas sit aspernatur aut odit aut fugit, sed quia consntur magni dolores eos qui ratione</p>
  </div>
  <div class="step" style="left:819px">
    <div class="step-icon"><svg width="40" height="40" viewBox="0 0 24 24" fill="none" stroke="#0255a3" stroke-width="2.2" stroke-linecap="round"><path d="M12 2v20"/><path d="M17 6.5c-1-1.3-2.8-2-5-2-2.8 0-4.5 1.4-4.5 3.3 0 4.6 9.5 2.4 9.5 7.4 0 2-1.9 3.3-5 3.3-2.3 0-4.1-.8-5-2.2"/></svg></div>
    <h3>Get Finance Fast</h3>
    <p>Nemo enim ipsam voluptatem quia voluptas sit aspernatur aut odit aut fugit, sed quia consntur magni dolores eos qui ratione</p>
  </div>
  <svg class="abs" style="left:390px;top:190px" width="80" height="40" viewBox="0 0 80 40"><path d="M4 22 Q40 0 70 24" stroke="#fff" stroke-width="3" fill="none"/><path d="M62 26 74 28 70 16z" fill="#fff"/></svg>
  <svg class="abs" style="left:752px;top:225px" width="80" height="40" viewBox="0 0 80 40"><path d="M4 28 Q40 40 68 10" stroke="#fff" stroke-width="3" fill="none"/><path d="M60 12 74 4 72 18z" fill="#fff"/></svg>
  <div class="btn-apply">APPLY NOW</div>
</section>

<section class="reviews">
  <h2 class="section-title" style="top:63px;font-size:27px">CUSTOMER REVIEWS</h2>
  <article class="review" style="left:129px">
    <blockquote>“ Lorem ipsum dolor sit amet, consectetur adipisicing elit, sed do eiusmod tempor incididunt ut labore et dolore magna aliqua Unde omnis, consequuntur.</blockquote>
    <div class="reviewer">
      <div class="avatar" role="img" aria-label="Reviewer portrait"></div>
      <div><div class="reviewer-name">Mara Ellison - Northgate Lending</div>
        <div class="stars"><span><svg width="11" height="11" viewBox="0 0 10 10"><path fill="#fff" d="m5 .5 1.4 2.9 3.1.4-2.3 2.2.6 3.1L5 7.6 2.2 9.1l.6-3.1L.5 3.8l3.1-.4z"/></svg></span><span><svg width="11" height="11" viewBox="0 0 10 10"><path fill="#fff" d="m5 .5 1.4 2.9 3.1.4-2.3 2.2.6 3.1L5 7.6 2.2 9.1l.6-3.1L.5 3.8l3.1-.4z"/></svg></span><span><svg width="11" height="11" viewBox="0 0 10 10"><path fill="#fff" d="m5 .5 1.4 2.9 3.1.4-2.3 2.2.6 3.1L5 7.6 2.2 9.1l.6-3.1L.5 3.8l3.1-.4z"/></svg></span><span><svg width="11" height="11" viewBox="0 0 10 10"><path fill="#fff" d="m5 .5 1.4 2.9 3.1.4-2.3 2.2.6 3.1L5 7.6 2.2 9.1l.6-3.1L.5 3.8l3.1-.4z"/></svg></span><span><svg width="11" height="11" viewBox="0 0 10 10"><path fill="#fff" d="m5 .5 1.4 2.9 3.1.4-2.3 2.2.6 3.1L5 7.6 2.2 9.1l.6-3.1L.5 3.8l3.1-.4z"/></svg></span></div>
      </div>
    </div>
  </article>
  <article class="review" style="left:650px">
    <blockquote>“ Lorem ipsum dolor sit amet, consectetur adipisicing elit, sed do eiusmod tempor incididunt ut labore et dolore magna aliqua Unde omnis, consequuntur.</blockquote>
    <div class="reviewer">
      <div class="avatar" role="img" aria-label="Reviewer portrait" style="background:radial-gradient(circle at 50% 40%,#b89a82,#5e4a3f)"></div>
      <div><div class="reviewer-name">Mara Ellison - Northgate Lending</div>
        <div class="stars"><span><svg width="11" height="11" viewBox="0 0 10 10"><path fill="#fff" d="m5 .5 1.4 2.9 3.1.4-2.3 2.2.6 3.1L5 7.6 2.2 9.1l.6-3.1L.5 3.8l3.1-.4z"/></svg></span><span><svg width="11" height="11" viewBox="0 0 10 10"><path fill="#fff" d="m5 .5 1.4 2.9 3.1.4-2.3 2.2.6 3.1L5 7.6 2.2 9.1l.6-3.1L.5 3.8l3.1-.4z"/></svg></span><span><svg width="11" height="11" viewBox="0 0 10 10"><path fill="#fff" d="m5 .5 1.4 2.9 3.1.4-2.3 2.2.6 3.1L5 7.6 2.2 9.1l.6-3.1L.5 3.8l3.1-.4z"/></svg></span><span><svg width="11" height="11" viewBox="0 0 10 10"><path fill="#fff" d="m5 .5 1.4 2.9 3.1.4-2.3 2.2.6 3.1L5 7.6 2.2 9.1l.6-3.1L.5 3.8l3.1-.4z"/></svg></span><span><svg width="11" height="11" viewBox="0 0 10 10"><path fill="#fff" d="m5 .5 1.4 2.9 3.1.4-2.3 2.2.6 3.1L5 7.6 2.2 9.1l.6-3.1L.5 3.8l3.1-.4z"/></svg></span></div>
      </div>
    </div>
  </article>
</section>

<section class="partners" aria-label="Partner marks">
  <div class="partner-mark" style="left:137px;width:64px"></div>
  <div class="partner-mark" style="left:258px;width:114px"></div>
  <div class="partner-mark" style="left:431px;width:96px"></div>
  <div class="partner-mark" style="left:595px;width:108px"></div>
  <div class="partner-mark" style="left:787px;width:84px"></div>
  <div class="partner-mark" style="left:942px;width:116px"></div>
</section>

<footer class="site-footer">
  <div class="footer-brand"><span class="brand-dot" style="width:56px;height:56px"></span><span class="brand-name" style="text-align:center">BRIGHTWELL FINANCE</span></div>
  <div class="footer-col"><h4 style="left:277px">CONTACTS US</h4></div>
  <div class="contact-line" style="top:72px"><svg width="12" height="16" viewBox="0 0 12 16"><path fill="#7fa7cf" d="M6 0a6 6 0 0 0-6 6c0 4.5 6 10 6 10s6-5.5 6-10a6 6 0 0 0-6-6zm0 8.5A2.5 2.5 0 1 1 6 3.5a2.5 2.5 0 0 1 0 5z"/></svg><span>Brightwell Finance P.O. Box 6120 Harbourton,<br>Coral Bay</span></div>
  <div class="contact-line" style="top:130px"><svg width="13" height="13" viewBox="0 0 24 24"><path fill="#7fa7cf" d="M6.6 10.8a15.1 15.1 0 0 0 6.6 6.6l2.2-2.2a1 1 0 0 1 1-.25 11.4 11.4 0 0 0 3.6.57 1 1 0 0 1 1 1V20a1 1 0 0 1-1 1A17 17 0 0 1 3 4a1 1 0 0 1 1-1h3.5a1 1 0 0 1 1 1c0 1.25.2 2.45.57 3.57a1 1 0 0 1-.25 1z"/></svg><span>Phone: +1300 482 719</span></div>
  <div class="contact-line" style="top:160px"><svg width="13" height="13" viewBox="0 0 24 24"><path fill="#7fa7cf" d="M2 5h20v14H2zm2 2v.5l8 5 8-5V7l-8 5z"/></svg><span>info@brightwellfinance.com.au</span></div>
  <div class="footer-col"><h4 style="left:624px">SIGN UP FOR NEWSLETTER</h4></div>
  <p class="newsletter-text">Get the latest updates on our courses and events: Notify Me</p>
  <div class="nl-input" style="top:117px">Enter Name</div>
  <div class="nl-input" style="top:167px">Enter Email</div>
  <div class="btn-subscribe">SUBSCRIBE</div>
  <div class="footer-col"><h4 style="left:970px">INFORMATION</h4></div>
  <ul class="info-links">
    <li>Bas Agent</li>
    <li>Payroll And Bookkeeping</li>
    <li>Credit File Repair</li>
    <li>Default Removals</li>
    <li>Debt Consolidation</li>
  </ul>
</footer>
<div class="copyright">©2015 - 2016 &nbsp;BRIGHTWELL FINANCE .. All Rights Reserved.</div>

</body>
</html>
```